Software Consulting Business Needs a Powerpoint Design

We need a powerpoint template design for a software consulting company called Tessel7, that we can use for a corporate overview presentation.

Our website/logo can be found at www.tessel7-demo.net which should give you a good idea of our color scheme.

Here is a link to a zip file with the logos in AI format:

http://www.tessel7-demo.net/logo/T7_Logo_Illustrator.zip

Here is a link to the Din font:

http://www.tessel7-demo.net/logo/Din.zip

Sorry for delay. I was on vacation. A decision will be made by end of the week. Thanks!

Software

```html
<!DOCTYPE html>
<html lang="en">
<head>
<meta charset="utf-8">
<title>Tessel7 — About Us</title>
<link rel="stylesheet" href="https://fonts.googleapis.com/css2?family=Carlito:wght@400;700&display=swap">
<style>
  :root {
    --brand-red: #8c1010;
    --banner-dark: #4a0a0c;
    --banner-mid: #7a1a1c;
    --navy: #1f3655;
    --navy-light: #3b5f88;
    --paper: #f3f1ee;
    --backdrop-light: #e9e9e9;
    --backdrop-dark: #cfd0d2;
    --ink: #111111;
    --white: #ffffff;
  }
  * { margin: 0; padding: 0; box-sizing: border-box; }
  html, body { width: 1200px; height: 900px; overflow: hidden; }
  body { font-family: "Carlito", "Calibri", sans-serif; color: var(--ink); }

  .slide {
    position: relative;
    width: 1200px;
    height: 900px;
    overflow: hidden;
  }
  .backdrop {
    position: absolute; inset: 0;
    background: radial-gradient(ellipse at 50% 45%, var(--backdrop-light) 0%, #dcdcdd 60%, var(--backdrop-dark) 100%);
  }
  .header-banner {
    position: absolute; left: 0; top: 0; width: 1200px; height: 112px;
    background: linear-gradient(180deg, var(--banner-mid) 0%, var(--banner-dark) 100%);
    border-bottom: 3px solid #b9b9bb;
  }
  .brand-tab {
    position: absolute; left: 0; top: 0; width: 1200px; height: 120px;
  }
  .brand-name {
    position: absolute; left: 968px; top: 50px; width: 200px;
    font-weight: 700; font-size: 29px; letter-spacing: 1.5px;
    color: var(--white); text-align: center; line-height: 36px;
  }
  .slide-title {
    position: absolute; left: 0; top: 168px; width: 1250px;
    text-align: center;
    font-weight: 700; font-size: 56px; line-height: 64px;
    color: var(--brand-red);
  }
  .title-rule {
    position: absolute; left: 62px; top: 237px; width: 1092px; height: 10px;
    border-top: 5px solid var(--brand-red);
    border-bottom: 2px solid var(--brand-red);
  }
  .content-panel {
    position: absolute; left: 122px; top: 250px; width: 956px; height: 498px;
    background: var(--paper);
  }
  .content-text {
    position: absolute; left: 202px; top: 364px; width: 826px;
    font-size: 37px; line-height: 56px;
    text-align: justify;
  }
  .page-number {
    position: absolute; left: 1126px; top: 809px; width: 52px; height: 52px;
  }
  .page-number span {
    position: absolute; inset: 0;
    display: flex; align-items: center; justify-content: center;
    color: var(--white); font-size: 16px;
  }
  .footer-bar {
    position: absolute; left: 0; top: 870px; width: 1200px; height: 30px;
    background: var(--navy);
    border-top: 3px solid var(--navy-light);
  }
</style>
</head>
<body>
  <main class="slide">
    <div class="backdrop" role="img" aria-label="Soft grey background with a faint grid texture"></div>
    <div class="header-banner" role="img" aria-label="Dark red header banner with a subtle technical grid pattern"></div>

    <svg class="brand-tab" viewBox="0 0 1200 120" aria-hidden="true">
      <path d="M862 38 Q850 38 846 50 L870 106 L1200 106 L1200 38 Z" fill="#ffffff" opacity="0.9"/>
      <path d="M868 43 Q858 43 855 52 L876 100 L1200 100 L1200 43 Z" fill="var(--navy)"/>
    </svg>
    <div class="brand-name">TESSEL7</div>

    <h1 class="slide-title">About Us</h1>
    <div class="title-rule"></div>

    <section class="content-panel" aria-hidden="true"></section>
    <p class="content-text">We are a software company specializing in enterprise technology. Founded in 2007, we deliver our products, world-class services, customized solutions, and timely support across all sectors of industry</p>

    <div class="page-number">
      <svg width="52" height="52" viewBox="0 0 52 52" aria-hidden="true">
        <rect x="8" y="8" width="36" height="36" transform="rotate(45 26 26)" fill="var(--brand-red)"/>
      </svg>
      <span>16</span>
    </div>

    <div class="footer-bar"></div>
  </main>
</body>
</html>
```